Business card update

Opening a subsidiary of my company in the USA and need to update my logo.
Updates

Reason: Give more time to a good design.

I made a mistake on my briefing. It's only the business card. Thanks for alerting me on the mistake.

All the best

Leopoldo

Target Market(s)

We are an Executive Search company and our target audience are executives in large corporations.

Industry/Entity Type

Business

Requirements
Must have
• Keep the logo. In the US the company is called Declan Harrow Executive Search.

```html
<!DOCTYPE html>
<html lang="en">
<head>
<meta charset="utf-8">
<title>Declan Harrow Executive Search – Business Card</title>
<link rel="stylesheet" href="https://fonts.googleapis.com/css2?family=Questrial&family=Open+Sans:wght@300;400&display=swap">
<style>
  :root {
    --teal: #2aa9b2;
    --teal-deep: #1f9aa3;
    --card: #ffffff;
    --ink: #555a5e;
    --ink-dark: #333638;
    --shadow: rgba(0, 60, 66, 0.35);
  }
  * { box-sizing: border-box; margin: 0; padding: 0; }
  html, body {
    width: 900px;
    height: 1200px;
    overflow: hidden;
  }
  body {
    background: var(--teal);
    font-family: "Open Sans", Arial, sans-serif;
    position: relative;
  }
  .card {
    position: absolute;
    left: 170px;
    width: 560px;
    height: 320px;
    background: var(--card);
    box-shadow: 0 14px 30px var(--shadow);
  }
  .card--front { top: 200px; }
  .card--back  { top: 640px; }

  .card__frame {
    position: absolute;
    inset: 12px;
    border: 1.5px dotted var(--teal);
  }

  /* Front: wordmark */
  .wordmark {
    position: absolute;
    left: 0; right: 0;
    top: 112px;
    text-align: center;
  }
  .wordmark__rule {
    width: 400px;
    height: 1.5px;
    margin: 0 auto 14px;
    background: var(--teal);
  }
  .wordmark__name {
    font-family: "Questrial", "Century Gothic", sans-serif;
    font-size: 34px;
    letter-spacing: 5px;
    color: var(--ink);
    font-weight: 400;
  }
  .wordmark__tagline {
    margin-top: 16px;
    font-size: 14px;
    font-weight: 400;
    color: var(--teal);
  }

  /* Back: contact details */
  .contact {
    position: absolute;
    left: 54px;
    top: 50px;
  }
  .contact__name {
    font-size: 26px;
    font-weight: 400;
    color: var(--ink);
  }
  .contact__role {
    margin-top: 4px;
    font-size: 13px;
    color: var(--teal);
  }
  .contact__dash {
    width: 22px;
    height: 2px;
    margin: 22px 0 22px;
    background: var(--ink-dark);
  }
  .contact__list {
    list-style: none;
    font-size: 12.5px;
    line-height: 1.75;
    color: var(--teal);
  }
  .contact__list li::before {
    content: "•";
    margin-right: 8px;
    color: var(--ink);
  }
</style>
</head>
<body>
  <section class="card card--front" aria-label="Business card front">
    <div class="card__frame"></div>
    <div class="wordmark">
      <div class="wordmark__rule"></div>
      <div class="wordmark__name">DECLAN HARROW</div>
      <div class="wordmark__tagline">Executive Search</div>
    </div>
  </section>

  <section class="card card--back" aria-label="Business card back">
    <div class="contact">
      <h1 class="contact__name">Leopoldo S. Harrow</h1>
      <p class="contact__role">Co-Founder &amp; CEO</p>
      <div class="contact__dash"></div>
      <ul class="contact__list">
        <li>lharrow@dhexecutivesearch.com</li>
        <li>4870 Coral Harbor Blvd Suite 310</li>
        <li>Bay Harbor FL 33154</li>
        <li>305 555-0148</li>
        <li>www.dhexecutivesearch.com</li>
      </ul>
    </div>
  </section>
</body>
</html>
```